Crit postcard design

I am in charge of getting a postcard 5x7 designed for 14 artists having a gallery exhibition. We would like to use our
photo(s) with the 14 names on the front. Back of card would have gallery information.
Am sending jpeg of a past card, four images to choose from and the text for back of card.

Artists

```html
<!DOCTYPE html>
<html lang="en">
<head>
<meta charset="utf-8">
<title>Fourteen Painters</title>
<link rel="stylesheet" href="https://fonts.googleapis.com/css2?family=Righteous&family=Alfa+Slab+One&family=Oswald:wght@500&family=Audiowide&family=Bodoni+Moda:wght@700&family=Russo+One&family=Bowlby+One&family=Archivo+Black&family=Francois+One&family=Anton&family=Cinzel:wght@400&display=swap">
<style>
  :root {
    --grey: #8e8e8e;
    --grey-light: #c9c9c9;
    --ink: #1e1e1e;
    --yellow: #d8c21a;
    --mustard: #c9b01c;
    --blue: #2c3591;
    --sky: #35b3d6;
    --teal: #2a8c8a;
    --red: #e8303f;
    --orange: #f07f12;
    --white: #ffffff;
  }
  html, body {
    margin: 0;
    padding: 0;
    overflow: hidden;
    background: var(--white);
  }
  .postcard {
    position: relative;
    width: 1200px;
    height: 720px;
    overflow: hidden;
  }
  .postcard__photo {
    position: absolute;
    inset: 0;
    width: 100%;
    height: 100%;
  }
  .artist {
    position: absolute;
    margin: 0;
    line-height: 1;
    white-space: nowrap;
    color: transparent;
    -webkit-background-clip: text;
    background-clip: text;
  }
  .artist--halvoran {
    left: 58px; top: 34px;
    font: 70px "Righteous", sans-serif;
    background-image: linear-gradient(90deg, var(--mustard) 0 26%, var(--sky) 26% 42%, var(--mustard) 42%);
  }
  .artist--tollerd {
    left: 406px; top: 86px;
    font: 64px "Alfa Slab One", serif;
    transform: scaleX(0.85); transform-origin: left top;
    background-image: linear-gradient(90deg, var(--blue) 0 30%, var(--yellow) 30% 50%, var(--red) 50% 80%, var(--blue) 80%);
  }
  .artist--reed {
    left: 734px; top: 10px;
    font: 500 104px "Oswald", sans-serif;
    transform: scaleX(0.75); transform-origin: left top;
    background-image: linear-gradient(100deg, var(--ink) 0 25%, var(--yellow) 25% 55%, var(--orange) 55% 75%, var(--yellow) 75%);
  }
  .artist--vos {
    left: 978px; top: 70px;
    font: 80px "Audiowide", sans-serif;
    background-image: linear-gradient(160deg, var(--yellow) 0 30%, var(--blue) 30% 60%, var(--red) 60%);
  }
  .artist--hoffstedt {
    left: 56px; top: 174px;
    font: 700 60px "Bodoni Moda", serif;
    letter-spacing: 0.06em;
    background-image: linear-gradient(90deg, var(--yellow) 0 20%, var(--sky) 20% 60%, var(--blue) 60%);
  }
  .artist--lun {
    left: 694px; top: 160px;
    font: 60px "Russo One", sans-serif;
    background-image: linear-gradient(90deg, var(--blue) 0 40%, var(--orange) 40%);
  }
  .artist--pelder {
    left: 408px; top: 208px;
    font: 56px "Alfa Slab One", serif;
    background-image: linear-gradient(90deg, var(--red) 0 12%, var(--ink) 12% 40%, var(--teal) 40% 80%, var(--ink) 80%);
  }
  .artist--brightwell {
    left: 736px; top: 232px;
    font: 60px "Alfa Slab One", serif;
    transform: scaleX(0.96); transform-origin: left top;
    background-image: linear-gradient(90deg, var(--blue) 0 18%, var(--ink) 18% 40%, var(--yellow) 40% 55%, var(--red) 55% 75%, var(--orange) 75%);
  }
  .artist--morrow {
    left: 20px; top: 292px;
    font: 52px "Bowlby One", sans-serif;
    transform: scaleX(0.86); transform-origin: left top;
    background-image: linear-gradient(90deg, var(--sky) 0 20%, var(--yellow) 20% 45%, var(--red) 45% 75%, var(--ink) 75%);
  }
  .artist--skovgard {
    left: 274px; top: 296px;
    font: 60px "Archivo Black", sans-serif;
    transform: scaleX(0.82); transform-origin: left top;
    background-image: linear-gradient(90deg, var(--yellow) 0 12%, var(--ink) 12%);
  }
  .artist--ashlin {
    left: 600px; top: 304px;
    font: 72px "Francois One", sans-serif;
    background-image: linear-gradient(90deg, var(--blue) 0 35%, var(--orange) 35% 60%, var(--ink) 60%);
  }
  .artist--penfold {
    left: 918px; top: 300px;
    font: 78px "Anton", sans-serif;
    background-image: linear-gradient(180deg, var(--ink) 0 50%, var(--yellow) 50% 80%, var(--ink) 80%);
  }
  .artist--westmere {
    left: 189px; top: 396px;
    font: 44px "Alfa Slab One", serif;
    background-image: linear-gradient(180deg, var(--ink) 0 55%, var(--grey-light) 55%);
  }
  .artist--elliot {
    left: 588px; top: 400px;
    font: 66px "Cinzel", serif;
    background-image: linear-gradient(90deg, var(--grey) 0 60%, var(--ink) 60%);
  }
  .show-title {
    position: absolute;
    left: 48px; top: 622px;
    margin: 0;
    font: 400 84px "Cinzel", serif;
    line-height: 1;
    letter-spacing: 0.15em;
    white-space: nowrap;
    color: var(--white);
    -webkit-text-stroke: 1.5px var(--ink);
  }
</style>
</head>
<body>
<main class="postcard">
  <svg class="postcard__photo" viewBox="0 0 1200 720" role="img" aria-label="Photograph of dripped paint in yellow, blue, red and orange with a palette knife and a white paintbrush, softened behind the names">
    <defs>
      <linearGradient id="photoTone" x1="0" y1="0" x2="1" y2="1">
        <stop offset="0" stop-color="#b9b6a4"/>
        <stop offset="0.35" stop-color="#a9a9ad"/>
        <stop offset="0.6" stop-color="#c7bba6"/>
        <stop offset="1" stop-color="#efcfa8"/>
      </linearGradient>
      <radialGradient id="warmGlow" cx="0.85" cy="0.3" r="0.5">
        <stop offset="0" stop-color="#f6c996" stop-opacity="0.8"/>
        <stop offset="1" stop-color="#f6c996" stop-opacity="0"/>
      </radialGradient>
    </defs>
    <rect width="1200" height="720" fill="url(#photoTone)"/>
    <rect width="1200" height="720" fill="url(#warmGlow)"/>
  </svg>

  <p class="artist artist--halvoran">Halvoran</p>
  <p class="artist artist--tollerd">Tollerd</p>
  <p class="artist artist--reed">Reed</p>
  <p class="artist artist--vos">Vos</p>
  <p class="artist artist--hoffstedt">Hoffstedt</p>
  <p class="artist artist--lun">LUN</p>
  <p class="artist artist--pelder">Pelder</p>
  <p class="artist artist--brightwell">Brightwell</p>
  <p class="artist artist--morrow">Morrow</p>
  <p class="artist artist--skovgard">SKOVGARD</p>
  <p class="artist artist--ashlin">Ashlin</p>
  <p class="artist artist--penfold">Penfold</p>
  <p class="artist artist--westmere">Westmere</p>
  <p class="artist artist--elliot">ELLIOT</p>

  <h1 class="show-title">FOURTEEN PAINTERS</h1>
</main>
</body>
</html>
```